Heritage Depot Business Cards

Require a business card design. <br/><br/>Needs to include logo (either round or long version) plus these details:<br/>Maya Corvell<br/>Heritage Depot<br/>maya@brightmarttrade.com.au<br/>02 6418 7395<br/>PO Box Glenfarrow NSW 2791<br/>www.heritagedepot.com.au<br/><br/>I need in an editable format so that I can create for multiple staff members. <br/><br/>

Target Market(s)

We are an online store selling renovation products to home owners are builders. Looking for a classic classy design.

Industry/Entity Type

Home And Garden

Contact Information for Business Card

Maya Corvell
Heritage Depot
maya@brightmarttrade.com.au
02 6418 7395
PO Box Glenfarrow NSW 2791
www.heritagedepot.com.au

Colors

Designer to choose colors to be used in the design.

Requirements
Must have
• Must include Logo.

```html
<!DOCTYPE html>
<html lang="en">
<head>
<meta charset="utf-8">
<title>Heritage Depot Business Cards</title>
<link href="https://fonts.googleapis.com/css2?family=Alegreya:wght@500&family=Josefin+Sans:wght@400;600&family=Raleway:wght@400&display=swap" rel="stylesheet">
<style>
  :root {
    --page-bg: #ececec;
    --card-top: #ffffff;
    --card-bottom: #eeeeef;
    --green-strong: #00bf7c;
    --green-soft: #9fe6cd;
    --ink: #1e1e1e;
    --navy: #1f3352;
    --rule: #e2e2e2;
  }
  * { margin: 0; padding: 0; box-sizing: border-box; }
  html, body { width: 1200px; height: 1200px; overflow: hidden; }
  body { background: var(--page-bg); position: relative; }

  .card {
    position: absolute;
    left: 227px;
    width: 750px;
    height: 450px;
    background: linear-gradient(180deg, var(--card-top), var(--card-bottom));
    overflow: hidden;
  }
  .card--front { top: 127px; }
  .card--back { top: 648px; }

  .card__accents { position: absolute; inset: 0; }

  .brand-seal {
    position: absolute;
    left: 258px; top: 83px;
    width: 262px; height: 262px;
    border: 1.2px solid var(--ink);
    border-radius: 50%;
    display: flex; align-items: center; justify-content: center;
  }
  .brand-seal__name {
    font-family: "Alegreya", serif;
    font-weight: 500;
    font-size: 40px;
    line-height: 1.05;
    color: var(--ink);
    text-align: left;
    margin-top: 50px;
  }

  .brand-line {
    position: absolute;
    left: 50px; top: 236px;
    display: flex; align-items: center; gap: 12px;
  }
  .brand-line__mark {
    width: 26px; height: 26px;
    border: 1.2px solid var(--ink);
    border-radius: 50%;
  }
  .brand-line__name {
    font-family: "Alegreya", serif;
    font-weight: 500;
    font-size: 34px;
    color: var(--ink);
  }

  .divider {
    position: absolute;
    left: 377px; top: 125px;
    width: 1px; height: 225px;
    background: var(--rule);
  }

  .person {
    position: absolute;
    left: 413px; top: 146px;
  }
  .person__name {
    font-family: "Josefin Sans", sans-serif;
    font-weight: 400;
    font-size: 30px;
    letter-spacing: 1.5px;
    color: var(--navy);
    line-height: 1;
  }
  .person__role {
    font-family: "Josefin Sans", sans-serif;
    font-size: 20px;
    color: var(--navy);
    margin-top: 6px;
  }

  .contacts {
    position: absolute;
    left: 408px; top: 226px;
    list-style: none;
    font-family: "Raleway", sans-serif;
    font-size: 12.5px;
    color: var(--navy);
  }
  .contacts li {
    display: flex; align-items: center; gap: 14px;
    height: 25px;
  }
  .contacts li:last-child { margin-top: 7px; }
  .contacts svg { width: 13px; height: 13px; fill: var(--navy); flex: none; }
</style>
</head>
<body>

<section class="card card--front">
  <svg class="card__accents" viewBox="0 0 750 450" role="img" aria-label="Scattered green square pattern in the top-left and bottom-right corners">
    <defs>
      <linearGradient id="accentTL" x1="0" y1="0" x2="1" y2="0.6">
        <stop offset="0" stop-color="var(--green-strong)"/>
        <stop offset="1" stop-color="var(--green-soft)" stop-opacity="0.5"/>
      </linearGradient>
      <linearGradient id="accentBR" x1="1" y1="1" x2="0" y2="0.4">
        <stop offset="0" stop-color="var(--green-strong)"/>
        <stop offset="1" stop-color="var(--green-soft)" stop-opacity="0.5"/>
      </linearGradient>
    </defs>
    <polygon points="0,0 380,0 0,150" fill="url(#accentTL)"/>
    <polygon points="750,325 750,450 390,450" fill="url(#accentBR)"/>
  </svg>
  <div class="brand-seal">
    <p class="brand-seal__name">Heritage<br>Depot</p>
  </div>
</section>

<section class="card card--back">
  <svg class="card__accents" viewBox="0 0 750 450" role="img" aria-label="Scattered green square pattern in the top-left and bottom-right corners">
    <defs>
      <linearGradient id="accentTL2" x1="0" y1="0" x2="1" y2="0.6">
        <stop offset="0" stop-color="var(--green-strong)"/>
        <stop offset="1" stop-color="var(--green-soft)" stop-opacity="0.5"/>
      </linearGradient>
      <linearGradient id="accentBR2" x1="1" y1="1" x2="0" y2="0.4">
        <stop offset="0" stop-color="var(--green-strong)"/>
        <stop offset="1" stop-color="var(--green-soft)" stop-opacity="0.5"/>
      </linearGradient>
    </defs>
    <polygon points="0,0 380,0 0,150" fill="url(#accentTL2)"/>
    <polygon points="750,325 750,450 390,450" fill="url(#accentBR2)"/>
  </svg>

  <div class="brand-line">
    <span class="brand-line__mark"></span>
    <span class="brand-line__name">Heritage Depot</span>
  </div>

  <div class="divider"></div>

  <div class="person">
    <h1 class="person__name">MAYA CORVELL</h1>
    <p class="person__role">Director</p>
  </div>

  <ul class="contacts">
    <li>
      <svg viewBox="0 0 16 16" aria-hidden="true"><path d="M3.6 1.5l2.2 2.6-1.2 1.7c.9 2 2.4 3.5 4.4 4.4l1.7-1.2 2.6 2.2-1.3 2.3C6.8 13.3 2.7 9.2 1.3 3.1z"/></svg>
      <span>02 6418 7395</span>
    </li>
    <li>
      <svg viewBox="0 0 16 16" aria-hidden="true"><path d="M1 3.5h14v9H1z M1.8 4.2L8 9l6.2-4.8" fill="none" stroke="var(--navy)" stroke-width="1.6"/></svg>
      <span>maya@brightmarttrade.com.au</span>
    </li>
    <li>
      <svg viewBox="0 0 16 16" aria-hidden="true"><circle cx="8" cy="8" r="6.5" fill="none" stroke="var(--navy)" stroke-width="1.5"/><path d="M5 4.5c1.5 0 2 1.5 1 2.5s.5 2.5 2 2.5 1 3 0 3.5M10 3c.5 1 1.5 1.5 2.5 1.5"/></svg>
      <span>www.heritagedepot.com.au</span>
    </li>
    <li>
      <svg viewBox="0 0 16 16" aria-hidden="true"><path d="M8 1a5 5 0 0 0-5 5c0 3.8 5 9 5 9s5-5.2 5-9a5 5 0 0 0-5-5zm0 7a2 2 0 1 1 0-4 2 2 0 0 1 0 4z"/></svg>
      <span>PO Box Glenfarrow NSW 2791</span>
    </li>
  </ul>
</section>

</body>
</html>
```